Design cover for information booklet
I am looking for a design for the front and back cover of an information booklet. Also an inside page basic design.
The booklet will contain 10 double sided pages providing information on weight loss surgery.
See my website www.brevinmarsh.com.au for what I do and typical colour themes.
I would also like some theming/illustration which can be utilised on each inside page of the booklet, rather than the pages just being blank with text etc. What would a blank page on this inside of the booklet look like under the design theme that you have created?
My company is Kestrel Institute for Metabolic Surgery. You will find uploaded a Logo for Kestrel Institute for Metabolic Surgery as well as my other logo which is my name “Brevin Marsh, etc.”. The Kestrel Institute for Metabolic Surgery logo should be utilised. The other logo (Brevin Marsh) is optional.
The front cover should contain the following text as minimum:
Kestrel Institute for Metabolic Surgery
Mr Brevin Marsh MBBS FRACS GradCert (Health Stats)
Our tagline is “Experience, Expertise and Empathy”. This should probably be on the front cover also.
The back cover contains (as a minimum) our address, phone number, fax number:
Suite 17, Level 3
Tallowgate Northern Hospital
9 Pemberly Road, Fernwick VIC 3174
Phone: 03 9412 6083
Fax: 03 9417 2865
Email: info@kestrelims.com.au
The files should be in a form whereby the text can be edited and changed if need be.
1. problems with initial graphical attachments - Artforge end 2. several requests by designers for extension

```html
<!DOCTYPE html>
<html lang="en">
<head>
<meta charset="utf-8">
<title>Kestrel Institute for Metabolic Surgery – Booklet Covers and Inside Page</title>
<link rel="stylesheet" href="https://fonts.googleapis.com/css2?family=Oswald:wght@300;400;700&family=Open+Sans:wght@400;600&display=swap">
<style>
  :root{
    --backdrop:#03a89e;
    --teal:#1a796f;
    --teal-dark:#13655c;
    --teal-light:#238a7f;
    --grey:#77777b;
    --ink:#2b2b2b;
    --white:#ffffff;
    --photo-a:#b9c2c4;
    --photo-b:#6f8a9c;
  }
  *{margin:0;padding:0;box-sizing:border-box}
  html,body{width:1200px;height:1200px;overflow:hidden}
  body{background:var(--backdrop);position:relative;font-family:"Oswald",sans-serif}
  .page{position:absolute;width:377px;height:529px;background:var(--white);overflow:hidden;box-shadow:0 2px 6px rgba(0,0,0,.12)}
  .page svg.art{position:absolute;left:0;top:0;width:100%;height:100%}
  .front{left:187px;top:53px}
  .back{left:636px;top:53px}
  .inside{left:414px;top:619px}

  .brand{position:absolute;display:flex;align-items:center;gap:6px;color:var(--teal);font-family:"Oswald",sans-serif;font-weight:400;white-space:nowrap}
  .brand .mark-square{width:26px;height:26px;background:var(--teal);flex:none}
  .brand .mark-circle{width:22px;height:22px;border-radius:50%;background:var(--teal);flex:none}
  .brand-institute{left:17px;top:17px;font-size:10px;line-height:12px;text-transform:uppercase;letter-spacing:.3px}
  .brand-surgeon{left:204px;top:19px;font-size:15px;text-transform:uppercase;letter-spacing:.6px}

  .headline{position:absolute;right:15px;top:80px;font-size:40px;font-weight:700;color:var(--teal);letter-spacing:.5px;line-height:44px;white-space:nowrap}
  .tagline{position:absolute;left:96px;top:124px;font-size:20px;font-weight:300;color:var(--ink);line-height:26px;letter-spacing:.2px;white-space:nowrap}
  .web{position:absolute;right:17px;bottom:12px;font-size:9px;color:var(--white);letter-spacing:.4px;font-weight:300;white-space:nowrap}

  .back-brand{position:absolute;left:0;width:100%;top:420px;display:flex;justify-content:center;align-items:center;gap:6px;color:var(--white);font-size:10px;text-transform:uppercase;letter-spacing:.4px;white-space:nowrap}
  .back-brand .mark-square{width:22px;height:22px;border:2px solid var(--white);flex:none}
  .contact{position:absolute;top:488px;font-family:"Open Sans",sans-serif;font-size:5.5px;line-height:8px;color:var(--white);white-space:nowrap;font-style:normal}
  .contact-address{left:84px;padding-left:11px}
  .contact-address svg{position:absolute;left:0;top:6px;width:7px;height:9px}
  .contact-lines{left:204px;list-style:none}
  .contact-lines li{display:flex;align-items:center;gap:6px}
  .contact-lines svg{width:6px;height:6px;flex:none}

  .inside-bar{position:absolute;left:0;top:17px;width:86px;height:7px;background:var(--teal)}
  .page-number{position:absolute;right:14px;top:14px;font-family:"Open Sans",sans-serif;font-size:6px;color:#8a8a8a}
  .inside .brand-surgeon{left:18px;top:490px;font-size:13px}
  .inside .brand-surgeon .mark-circle{width:20px;height:20px}
  .theme-illustration{position:absolute;left:303px;top:467px;width:57px;height:48px;border-radius:3px;background:linear-gradient(160deg,#f3c9a4 0%,#6fb2c9 55%,#2f8a80 100%)}
</style>
</head>
<body>

<!-- Front cover -->
<section class="page front">
  <svg class="art" viewBox="0 0 314 441" preserveAspectRatio="none" aria-hidden="true">
    <defs>
      <linearGradient id="theatre" x1="0" y1="0" x2="1" y2="1">
        <stop offset="0" stop-color="var(--photo-a)"/>
        <stop offset="1" stop-color="var(--photo-b)"/>
      </linearGradient>
    </defs>
    <polygon points="0,134 314,256 314,441 0,441" fill="url(#theatre)" role="img" aria-label="Photograph of surgeons at work in an operating theatre"/>
    <polygon points="314,262 314,441 0,441 110,372" fill="var(--teal)"/>
    <polygon points="0,302 110,372 0,441" fill="var(--teal-dark)"/>
  </svg>
  <div class="brand brand-institute"><span class="mark-square"></span><span>Kestrel Institute<br>for Metabolic Surgery</span></div>
  <div class="brand brand-surgeon"><span class="mark-circle"></span><span>Brevin Marsh</span></div>
  <h1 class="headline">EXPERIENCE</h1>
  <p class="tagline">EXPERTISE AND EMPATHY</p>
  <p class="web">WWW.KESTRELIMS.COM.AU</p>
</section>

<!-- Back cover -->
<section class="page back">
  <svg class="art" viewBox="0 0 315 441" preserveAspectRatio="none" aria-hidden="true">
    <polygon points="0,90 315,298 315,441 0,441" fill="var(--teal)"/>
    <polygon points="0,90 100,156 0,210" fill="var(--teal-light)"/>
    <polygon points="0,355 85,441 0,441" fill="var(--teal-dark)"/>
    <line x1="0" y1="89" x2="315" y2="297" stroke="#1c1c1c" stroke-width="3"/>
    <polygon points="113,0 315,0 315,135" fill="var(--grey)"/>
  </svg>
  <div class="back-brand"><span class="mark-square"></span><span>Kestrel Institute for Metabolic Surgery</span></div>
  <address class="contact contact-address">
    <svg viewBox="0 0 10 14"><path d="M5 0a5 5 0 0 0-5 5c0 4 5 9 5 9s5-5 5-9a5 5 0 0 0-5-5zm0 7a2 2 0 1 1 0-4 2 2 0 0 1 0 4z" fill="#fff"/></svg>
    Suite 17, Level 3<br>Tallowgate Northern Hospital<br>9 Pemberly Road, Fernwick VIC 3174
  </address>
  <ul class="contact contact-lines">
    <li><svg viewBox="0 0 10 10"><path d="M2 0l2 2-1 2 3 3 2-1 2 2-2 2C4 10 0 6 0 2z" fill="#fff"/></svg>03 9412 6083</li>
    <li><svg viewBox="0 0 10 10"><rect x="2" y="0" width="6" height="3" fill="#fff"/><rect x="0" y="3" width="10" height="5" rx="1" fill="#fff"/><rect x="2" y="7" width="6" height="3" fill="#fff"/></svg>03 9417 2865</li>
    <li><svg viewBox="0 0 10 10"><rect x="0" y="2" width="10" height="7" fill="#fff"/><path d="M0 2l5 4 5-4" stroke="#1a796f" fill="none"/></svg>info@kestrelims.com.au</li>
  </ul>
</section>

<!-- Inside page -->
<section class="page inside">
  <div class="inside-bar"></div>
  <span class="page-number">01</span>
  <div class="brand brand-surgeon"><span class="mark-circle"></span><span>Brevin Marsh</span></div>
  <div class="theme-illustration" role="img" aria-label="Small illustration of a surgical team beside an operating table"></div>
</section>

</body>
</html>
```